Contractor Business Card Design

Looking to have a card made that has a bold description of (KITCHENS, BASEMENTS, BATHROOMS)

Definition and layers a plus

Contact info is;

Mark T. Ellery
Elmhaven, MN 55010
Cell: 612-555-0147
website: www.cobaltfinishworks.example
Email: cobaltfinishworksmn@mailbox.example

colors: red, black, gray, white

Contact Information for Business Card

Contact info is;

Mark T. Ellery
Elmhaven, MN 55010
Cell: 612-555-0147

Colors
ec1f27

Requirements
Must have
• Looking for layers and definition
Nice to have
• Cards are planned to be printed on plastic cards

```html
<!DOCTYPE html>
<html lang="en">
<head>
<meta charset="utf-8">
<title>Cobalt Finish Works – Business Card</title>
<link rel="stylesheet" href="https://fonts.googleapis.com/css2?family=Arimo:wght@400;700&family=Montserrat:wght@700&display=swap">
<style>
  :root {
    --red: #ec1f27;
    --black: #111111;
    --gray-fill: #dadada;
    --gray-edge: #b9b9b9;
    --pink: #f2a3a3;
    --pink-pale: #f6c3c3;
    --white: #ffffff;
  }
  html, body {
    margin: 0;
    padding: 0;
    width: 1200px;
    height: 686px;
    overflow: hidden;
    background: var(--white);
  }
  .card {
    position: relative;
    width: 1200px;
    height: 686px;
    background: var(--white);
    font-family: "Arimo", Arial, sans-serif;
  }
  .card p { margin: 0; }
  .brand-ring {
    position: absolute;
    left: 186px;
    top: 25px;
    width: 250px;
    height: 250px;
  }
  .brand-name {
    position: absolute;
    left: 60px;
    top: 300px;
    width: 502px;
    margin: 0;
    text-align: center;
    font-family: "Montserrat", Arial, sans-serif;
    font-weight: 700;
    font-size: 46px;
    line-height: 58px;
    letter-spacing: 3px;
    color: var(--black);
  }
  .services {
    position: absolute;
    left: 102px;
    top: 450px;
    margin: 0;
    padding: 0;
    list-style: none;
    font-weight: 700;
    font-size: 65px;
    line-height: 76px;
    color: var(--gray-fill);
    -webkit-text-stroke: 1.5px var(--gray-edge);
  }
  .services li { white-space: nowrap; }
  .services .kitchens { letter-spacing: 13.4px; }
  .services .basements { letter-spacing: 1.5px; }
  .services .bathrooms { letter-spacing: 0; }
  .services .plural {
    color: var(--pink);
    -webkit-text-stroke: 1.5px var(--pink);
  }
  .phone-icon {
    position: absolute;
    left: 637px;
    top: 252px;
    width: 62px;
    height: 62px;
  }
  .phone-number {
    position: absolute;
    right: 88px;
    top: 251px;
    font-weight: 700;
    font-size: 56px;
    line-height: 62px;
    letter-spacing: 4.5px;
    color: var(--red);
  }
  .location {
    position: absolute;
    left: 640px;
    top: 326px;
    font-size: 16px;
    line-height: 20px;
    color: var(--pink-pale);
  }
  .person-name {
    position: absolute;
    right: 90px;
    top: 312px;
    font-weight: 700;
    font-size: 32px;
    line-height: 38px;
    color: var(--black);
  }
  .person-name .dot { color: var(--red); }
  .divider {
    position: absolute;
    left: 637px;
    top: 362px;
    width: 471px;
    height: 12px;
    background: var(--pink);
    opacity: 0.8;
  }
  .contact-line {
    position: absolute;
    left: 646px;
    height: 46px;
    display: flex;
    align-items: center;
    gap: 27px;
    color: var(--red);
  }
  .contact-line svg { width: 46px; height: 46px; flex: none; }
  .contact-web { top: 502px; font-size: 29px; }
  .contact-mail { top: 560px; font-size: 23px; }
  .contact-line .join { color: var(--black); }
</style>
</head>
<body>
<main class="card">
  <svg class="brand-ring" viewBox="0 0 250 250" aria-hidden="true">
    <circle cx="125" cy="125" r="119" fill="none" stroke="var(--black)" stroke-width="6"/>
  </svg>
  <h1 class="brand-name">COBALT<br>FINISH WORKS</h1>

  <ul class="services">
    <li class="kitchens">KITCHEN<span class="plural">S</span></li>
    <li class="basements">BASEMENT<span class="plural">S</span></li>
    <li class="bathrooms">BATHROOM<span class="plural">S</span></li>
  </ul>

  <svg class="phone-icon" viewBox="0 0 62 62" aria-hidden="true">
    <circle cx="31" cy="31" r="30" fill="var(--red)"/>
    <circle cx="31" cy="31" r="25" fill="none" stroke="var(--white)" stroke-width="1.5"/>
    <path d="M22 19c2-1 3 0 4 2l2 4c1 2 0 3-1 4l-1 1c1 3 4 6 7 7l1-1c1-1 2-2 4-1l4 2c2 1 3 2 2 4-1 3-4 4-7 3-7-2-13-8-15-15-1-4 0-8 0-10z" fill="none" stroke="var(--white)" stroke-width="2.2" stroke-linejoin="round"/>
  </svg>
  <p class="phone-number">612-555-0147</p>
  <p class="location">Elmhaven, MN 55010</p>
  <p class="person-name">Mark T<span class="dot">.</span> Ellery</p>
  <div class="divider"></div>

  <p class="contact-line contact-web">
    <svg viewBox="0 0 46 46" aria-hidden="true">
      <circle cx="23" cy="23" r="22" fill="var(--red)"/>
      <g fill="none" stroke="var(--white)" stroke-width="2">
        <circle cx="23" cy="23" r="13"/>
        <ellipse cx="23" cy="23" rx="6" ry="13"/>
        <path d="M10 23h26M12 16h22M12 30h22M23 10v26"/>
      </g>
    </svg>
    <span>www<span class="join">.</span>cobaltfinishworks<span class="join">.</span>example</span>
  </p>
  <p class="contact-line contact-mail">
    <svg viewBox="0 0 46 46" aria-hidden="true">
      <circle cx="23" cy="23" r="22" fill="var(--red)"/>
      <rect x="12" y="15" width="22" height="16" fill="none" stroke="var(--white)" stroke-width="2"/>
      <path d="M12 15l11 9 11-9" fill="none" stroke="var(--white)" stroke-width="2"/>
    </svg>
    <span>cobaltfinishworksmn<span class="join">@</span>mailbox<span class="join">.</span>example</span>
  </p>
</main>
</body>
</html>
```